Your online mall needs the design of a banner ad

I need the design of a banner to publicize the website in local internet media. It has to attract the visitor from the middle, so it should be flashy but attractive. The website is an ecommerce. It is an online shopping center with more than 12,000 products and 18 different categories. The website is: www.vendalume.com Allowed file formats: JPG, PNG or GIF (never more than 30 seconds) File size: maximum 150KB Banner size: large rectangle 300x600 The banner should contain the following: -Logo de la brand (attached file) -Web site: www.vendalume.com - Phrase: "Your online shopping center" -Frame: "of 12,000 products of the leading brands of the market at the price of vendalume" -Frame: "Up to -70% Dto . " -Print key that can attract: REMATE (optional), UNCOVER (optional)

```html
<!DOCTYPE html>
<html lang="es">
<head>
<meta charset="utf-8">
<title>Vendalume banner</title>
<link href="https://fonts.googleapis.com/css2?family=Montserrat:wght@400;600;700;800&family=Anton&display=swap" rel="stylesheet">
<style>
  :root {
    --backdrop: #413d3e;
    --white: #ffffff;
    --navy: #2b3245;
    --orange: #f99d1c;
    --red: #e8202a;
    --blue-top: #1f9be0;
    --blue-bottom: #0a5fb0;
    --blue-dark: #0b4f93;
  }
  html, body {
    margin: 0;
    padding: 0;
    width: 1200px;
    height: 1200px;
    overflow: hidden;
    background: var(--backdrop);
  }
  .banner {
    position: absolute;
    left: 72px;
    top: 336px;
    width: 1143px;
    height: 571px;
    transform: scale(0.9231);
    transform-origin: top left;
    background: var(--white);
    overflow: hidden;
    box-shadow: -5px 5px 6px rgba(0,0,0,0.45);
    font-family: "Montserrat", sans-serif;
  }
  .backdrop-shapes { position: absolute; inset: 0; }
  .brand-dot {
    position: absolute;
    left: 32px; top: 36px;
    width: 60px; height: 60px;
    border-radius: 50%;
    background: var(--orange);
  }
  .brand-name {
    position: absolute;
    left: 114px; top: 34px;
    margin: 0;
    font-weight: 700;
    font-size: 52px;
    line-height: 1;
    color: var(--navy);
    letter-spacing: -1px;
    white-space: nowrap;
  }
  .brand-url {
    position: absolute;
    left: 117px; top: 100px;
    font-size: 21px;
    color: var(--navy);
  }
  .tagline {
    position: absolute;
    left: 58px; top: 146px;
    width: 314px; height: 39px;
    border-radius: 20px;
    background: var(--orange);
    color: var(--navy);
    font-weight: 700;
    font-size: 19px;
    line-height: 39px;
    text-align: center;
  }
  .photo {
    position: absolute;
  }
  .photo-cart {
    left: 72px; top: 241px;
    width: 290px; height: 295px;
    border-radius: 6px;
    background: linear-gradient(160deg, #f3d7de 0%, #e9e4d9 45%, #d8dbe0 100%);
  }
  .photo-model {
    left: 382px; top: 104px;
    width: 100px; height: 448px;
    border-radius: 40px 40px 8px 8px;
    background: linear-gradient(180deg, #e8ded6 0%, #c9dcef 30%, #8aa8cc 60%, #3f5f93 100%);
  }
  .count-pill {
    position: absolute;
    left: 577px; top: 80px;
    width: 412px; height: 57px;
    border: 3px solid var(--white);
    border-radius: 32px;
    background: var(--red);
    color: var(--white);
    font-weight: 700;
    font-size: 27px;
    line-height: 57px;
    text-align: center;
  }
  .headline {
    position: absolute;
    left: 572px; top: 146px;
    margin: 0;
    color: var(--white);
    font-weight: 700;
    font-size: 38px;
    line-height: 48px;
    letter-spacing: 0.3px;
  }
  .discount {
    position: absolute;
    left: 517px; top: 319px;
    width: 234px; height: 234px;
    border-radius: 50%;
    background: var(--white);
  }
  .discount-inner {
    position: absolute;
    left: 12px; top: 12px;
    width: 210px; height: 210px;
    border-radius: 50%;
    background: var(--red);
    color: var(--white);
    font-size: 37px;
    line-height: 48px;
    text-align: center;
    display: flex;
    flex-direction: column;
    justify-content: center;
  }
  .cta {
    position: absolute;
    left: 760px; top: 393px;
    width: 343px; height: 92px;
    border-radius: 8px;
    background: linear-gradient(180deg, var(--blue-top) 0%, var(--blue-bottom) 100%);
    text-decoration: none;
  }
  .cta-divider {
    position: absolute;
    left: 82px; top: 4px; bottom: 4px;
    width: 2px;
    background: var(--blue-dark);
  }
  .cta-icon { position: absolute; left: 22px; top: 24px; }
  .cta-label {
    position: absolute;
    left: 90px; right: 8px; top: 0;
    font-family: "Anton", sans-serif;
    font-size: 36px;
    line-height: 92px;
    color: var(--white);
    text-align: center;
    text-shadow: 2px 2px 0 #063a70;
    letter-spacing: 0.5px;
  }
</style>
</head>
<body>
  <div class="banner">
    <svg class="backdrop-shapes" width="1143" height="571" viewBox="0 0 1143 571">
      <polygon points="467,0 482,0 636,571 606,571" fill="var(--navy)"/>
      <polygon points="480,0 1143,0 1143,571 634,571" fill="var(--orange)"/>
      <polygon points="498,121 1092,121 1060,208 1092,294 542,294" fill="var(--navy)"/>
    </svg>

    <div class="brand-dot"></div>
    <h1 class="brand-name">Vendalume</h1>
    <div class="brand-url">www.vendalume.com</div>
    <div class="tagline">Tu centro comercial online</div>

    <div class="photo photo-cart" role="img" aria-label="Carrito de compra lleno de bolsas de colores y regalos con etiqueta de oferta"></div>
    <div class="photo photo-model" role="img" aria-label="Mujer sonriente de pie con camisa azul clara y vaqueros"></div>

    <div class="count-pill">+ DE 12.000 PRODUCTOS</div>
    <p class="headline">de las marcas lideres<br>del mercado a precio<br>de vendalume</p>

    <div class="discount">
      <div class="discount-inner"><span>Hasta</span><span>70% Dto</span></div>
    </div>

    <a class="cta" href="#">
      <svg class="cta-icon" width="42" height="46" viewBox="0 0 42 46">
        <polygon points="0,14 18,14 18,0 42,23 18,46 18,32 0,32" fill="var(--blue-dark)"/>
      </svg>
      <span class="cta-divider"></span>
      <span class="cta-label">COMPRA AHORA</span>
    </a>
  </div>
</body>
</html>
```